Redesign existing website.

I need a holidayhouse webdisain. Please review existing website: www.vaskemetsa.ee
I want to keep my logo.
Target Market(s)
Nature and sea enjoying holidaymakers, aged 30 to 70
Requirements
Must have
- 3 languages (English, Russian and Estonian)

```html
<!DOCTYPE html>
<html lang="et">
<head>
<meta charset="utf-8">
<title>Vaskemetsa Puhkemaja</title>
<link href="https://fonts.googleapis.com/css2?family=League+Gothic&family=Questrial&display=swap" rel="stylesheet">
<style>
:root{
  --teal:#0f9472;
  --teal-dark:#0b7f62;
  --teal-soft:rgba(22,150,112,.88);
  --blue:#1a9ce0;
  --white:#ffffff;
  --ink:#6b6b6b;
  --paper:#f6f6f4;
}
*{margin:0;padding:0;box-sizing:border-box}
html,body{width:720px;height:1200px;overflow:hidden}
body{position:relative;background:var(--paper);font-family:"Questrial",sans-serif;color:var(--ink)}
.abs{position:absolute}
.topbar{left:0;top:0;width:720px;height:21px;background:var(--teal)}
.social-dot{width:13px;height:13px;border-radius:50%;background:var(--white);top:4px}
.hero{left:0;top:21px;width:720px;height:441px;background:linear-gradient(180deg,#2d7fd0 0%,#6fb6ea 45%,#7fd3dc 62%,#efe6d8 72%,#e9ddc8 100%)}
.header{left:0;top:21px;width:720px;height:51px;background:rgba(255,255,255,.92)}
.brand{left:40px;top:38px;font-size:15px;color:var(--teal);letter-spacing:.5px}
.nav a{position:absolute;top:44px;font-size:9px;letter-spacing:.6px;color:var(--teal);text-decoration:none;transform:translateX(-50%)}
.hero-title{left:0;width:720px;top:200px;text-align:center;font-family:"League Gothic",sans-serif;font-size:66px;letter-spacing:2px;color:var(--white);text-shadow:2px 2px 2px rgba(0,0,0,.35);line-height:1}
.quote-btn{left:286px;top:288px;width:138px;height:32px;background:var(--blue);color:var(--white);font-size:12px;letter-spacing:.4px;text-align:center;line-height:31px;border-bottom:3px solid #137fbb}
.hero-note{left:170px;top:375px;width:368px;height:87px;background:var(--teal-soft);color:var(--white);font-size:9.2px;line-height:11.3px;letter-spacing:.5px;padding:22px 22px 0}
.welcome{left:0;width:720px;top:490px;text-align:center;font-size:9.5px;letter-spacing:.8px}
.site-title{left:0;width:720px;top:502px;text-align:center;font-family:"League Gothic",sans-serif;font-size:30px;letter-spacing:1px;color:var(--teal)}
.site-title span{color:var(--blue)}
.rule{left:320px;top:542px;width:82px;height:1px;background:#cfcfcf}
.feature{width:112px;text-align:center}
.feature-circle{width:112px;height:112px;border-radius:50%;background:var(--teal);display:flex;align-items:center;justify-content:center}
.feature-label{margin-top:18px;font-family:"League Gothic",sans-serif;font-size:15px;letter-spacing:.8px;color:var(--teal)}
.house-photo{left:111px;top:757px;width:186px;height:139px;background:#d9d9d6;padding:4px}
.house-photo div{width:100%;height:100%;background:linear-gradient(180deg,#5b86c6 0%,#8fb0d8 40%,#c9c2ad 60%,#4f6b34 100%)}
.about{left:319px;top:752px;width:338px;font-size:8.5px;line-height:11.3px;letter-spacing:.4px}
.about p{margin-bottom:11px}
.about .note{color:var(--teal)}
.footer{left:0;top:985px;width:720px;height:215px;background:var(--teal)}
.footer-head{left:0;top:985px;width:720px;height:36px;background:var(--teal-dark)}
.footer h3{position:absolute;top:998px;font-weight:normal;font-size:10.5px;letter-spacing:1px;color:var(--white)}
.flink{position:absolute;font-size:9.5px;letter-spacing:.6px;color:var(--white)}
.flink::before{content:"";display:inline-block;border-left:5px solid var(--white);border-top:3.5px solid transparent;border-bottom:3.5px solid transparent;margin-right:7px}
.sicon{width:15px;height:15px;border-radius:50%;background:var(--white)}
.slabel{font-size:9.5px;letter-spacing:.6px;color:var(--white)}
.footer-brand{left:545px;top:1068px;width:90px;text-align:center;font-size:14px;color:var(--white)}
.footer-rule{left:98px;top:1173px;width:532px;height:1px;background:rgba(255,255,255,.5)}
.address{left:98px;top:1181px;font-size:8.3px;letter-spacing:.5px;color:var(--white)}
</style>
</head>
<body>
<div class="abs hero" role="img" aria-label="Tropical beach photo with palm trees, a hammock, white sand and turquoise sea"></div>
<div class="abs topbar"></div>
<div class="abs social-dot" style="left:584px"></div>
<div class="abs social-dot" style="left:603px"></div>
<div class="abs social-dot" style="left:622px"></div>
<div class="abs header"></div>
<div class="abs brand">Vaskemetsa</div>
<nav class="nav">
  <a style="left:204px">TUTVUSTUS</a>
  <a style="left:290px">HINNAKIRI</a>
  <a style="left:373px">ASUKOHT</a>
  <a style="left:450px">GALERII</a>
  <a style="left:530px">HUVITAVAT</a>
  <a style="left:614px">KONTAKT</a>
</nav>
<h1 class="abs hero-title">CLEAN, FRESH, &amp; FUN</h1>
<div class="abs quote-btn">Get a free Quote</div>
<div class="abs hero-note">Lorem ipsum dolor sit amet, consectetur adipiscing elit. Integer fringilla mollis malesuada. vehicula enim sem fringilla mollis suada. Donec eu fringilla lectus. Integer dolor sit amet, consa-dipiscing elit mollis malesuada.</div>

<div class="abs welcome">Welcome to</div>
<h2 class="abs site-title">Vaskemetsa <span>Puhkemaja</span></h2>
<div class="abs rule"></div>

<div class="abs feature" style="left:136px;top:568px">
  <div class="feature-circle">
    <svg width="40" height="54" viewBox="0 0 40 54"><path d="M20 2C10 2 3 9.5 3 19c0 12 17 33 17 33s17-21 17-33C37 9.5 30 2 20 2z" fill="#fff"/><circle cx="20" cy="19" r="7" fill="#0f9472"/></svg>
  </div>
  <div class="feature-label">OUR LOCATION</div>
</div>
<div class="abs feature" style="left:304px;top:568px">
  <div class="feature-circle">
    <svg width="60" height="48" viewBox="0 0 60 48"><rect x="14" y="3" width="42" height="32" rx="2" fill="none" stroke="#fff" stroke-width="4" transform="rotate(6 35 19)"/><rect x="4" y="11" width="42" height="32" rx="2" fill="#0f9472" stroke="#fff" stroke-width="4"/><circle cx="15" cy="21" r="4" fill="#fff"/><path d="M8 39l12-12 7 7 6-6 9 11z" fill="#fff"/></svg>
  </div>
  <div class="feature-label">GALLERY</div>
</div>
<div class="abs feature" style="left:471px;top:568px">
  <div class="feature-circle">
    <svg width="78" height="44" viewBox="0 0 78 44"><path d="M2 30L22 8l12 14 9-9 28 29" fill="none" stroke="#fff" stroke-width="4" stroke-linejoin="round"/></svg>
  </div>
  <div class="feature-label">PICKS</div>
</div>

<div class="abs house-photo"><div role="img" aria-label="Photo of the white holiday house with a red tiled roof among trees"></div></div>
<div class="abs about">
  <p>Majutus 5-le puhkajale. Teid ootab mugav 2 magamistoaga puhkemaja. Asume põhjarannikul, Juminda poolsaarel, Kaasiku külas, Lahemaa rahvuspargis. Tallinnast vaid 61 km kaugusel. Kaasiku on sobiv koht mõnusaks, rahulikuks puhkuseks. Sillerdavat merd ja kauneid päikeseloojanguid võib nautida lausa maja aknast. Või veel parem – jalutad randa ja istud päevapäikese poolt kuumaks köetud kivile. Meie maja vastas olev rand on kivine, väikesele liivarannale 100m. Lahemaa toredad terviserajad on lähedal.</p>
  <p>Alumisel korrusel elutuba kamina ja kööginurgaga. Kööginurgas kõik vajalik toidu valmistamiseks - elektripliit, nõudepesumasin, mikrolaineahi, külmik, kohvimasin, veekeetja, nõud. Maja II-l korrusel on kaks magamistuba, duširuum pesumasinaga, WC. Merepoolses toas paarisvoodi, lisaks diivanvoodi. Teises toas 2 voodit ja lahtikäiv tugitool.</p>
  <p class="note">Pidustusteks puhkemaja välja ei rendita.</p>
</div>

<footer>
  <div class="abs footer"></div>
  <div class="abs footer-head"></div>
  <h3 style="left:110px">NAVIGATION</h3>
  <h3 style="left:289px">USEFUL INFO</h3>
  <h3 style="left:415px">STAY CONNECTED</h3>
  <span class="flink" style="left:110px;top:1038px">Tutvustus</span>
  <span class="flink" style="left:110px;top:1057px">Hinnakiri</span>
  <span class="flink" style="left:110px;top:1076px">Asukoht</span>
  <span class="flink" style="left:189px;top:1038px">Galerii</span>
  <span class="flink" style="left:189px;top:1057px">Huvitavat</span>
  <span class="flink" style="left:189px;top:1076px">Kontakt</span>
  <span class="flink" style="left:289px;top:1038px">Sitemap</span>
  <span class="flink" style="left:289px;top:1057px">F.A.Q</span>
  <span class="flink" style="left:289px;top:1076px">Privacy Policy</span>
  <div class="abs sicon" style="left:415px;top:1035px"></div>
  <span class="abs slabel" style="left:438px;top:1036px">Twitter</span>
  <div class="abs sicon" style="left:415px;top:1058px"></div>
  <span class="abs slabel" style="left:438px;top:1059px">Facebook</span>
  <div class="abs sicon" style="left:415px;top:1081px"></div>
  <span class="abs slabel" style="left:438px;top:1082px">Instagram</span>
  <div class="abs footer-brand">Vaskemetsa</div>
  <div class="abs footer-rule"></div>
  <div class="abs address">Rannatalu, Kaasiku village Kuusalu Parish, Harju 74712 / Tel. +372 55 10 2233 / e-mail: info@vaskemetsa.ee</div>
</footer>
</body>
</html>
```